Four in One (Flexible infographic for Content Management Industry)

See attachment.
A graphic depicting 4 products, where each can stand on its own and each can be combined with others, but where, if all are taken together, the best result is achieved (the "super product").
Intended use is web. See attached file as an example.
The most basic idea is as the attached diagram shows, where 4 rectangles are arranged in a quadrangle, with a middle rectangle in the center representing the combined 4 products. This concept is fine except it is a bit too obvious as it stands. We are looking for either a variation of this or another concept.
The audience is technical + professional + enterprise - NOT consumers. Hence the design should be conservative in nature.
We are aware of tools like as Canva or Pictogram where such graphics are available, but we are looking for something with a bit more imagination and flexibility.
This graphic should be targeted to web sites and be delivered with vector-based (SVG) graphics.

```html
<!DOCTYPE html>
<html lang="en">
<head>
<meta charset="utf-8">
<title>Four in One – Super Product</title>
<link rel="stylesheet" href="https://fonts.googleapis.com/css2?family=Barlow+Condensed:wght@600;700&family=Hind:wght@400&display=swap">
<style>
  :root {
    --purple: #7e72b0;
    --green: #8dc341;
    --teal: #02a59c;
    --blue: #167eb8;
    --orange: #ee7f1f;
    --ring: #e9ebea;
    --card: #f2f2f2;
    --ink: #333333;
    --icon: #8a8a8a;
    --btn-grey: #8c8c8c;
    --page: #ffffff;
  }
  * { box-sizing: border-box; margin: 0; padding: 0; }
  html, body { width: 1134px; height: 1200px; overflow: hidden; background: var(--page); }
  .canvas { position: relative; width: 1134px; height: 1200px; font-family: "Hind", Arial, sans-serif; color: var(--ink); }
  .diagram { position: absolute; inset: 0; }

  .card-title, .core-title {
    position: absolute; font-family: "Barlow Condensed", "Arial Narrow", sans-serif;
    font-weight: 700; color: #fff; text-align: center; letter-spacing: 0.2px;
  }
  .card-title { width: 444px; font-size: 30px; line-height: 72px; height: 72px; }
  .card-title.top-left { left: 70px; top: 56px; }
  .card-title.top-right { left: 619px; top: 52px; }
  .card-title.bottom-left { left: 70px; top: 1060px; }
  .card-title.bottom-right { left: 619px; top: 1060px; }

  .core-title { left: 392px; width: 350px; font-size: 74px; line-height: 90px; top: 505px; }

  .card-copy { position: absolute; font-size: 17.5px; line-height: 24.3px; }
  .card-copy p { white-space: nowrap; }
  .card-copy ul { list-style: none; }
  .card-copy li { position: relative; padding-left: 17px; white-space: nowrap; }
  .card-copy li::before {
    content: ""; position: absolute; left: 2px; top: 7px; width: 5px; height: 9px;
    border-right: 2.5px solid var(--ink); border-bottom: 2.5px solid var(--ink);
    transform: rotate(40deg);
  }
  .copy-doc { left: 102px; top: 159px; }
  .copy-security { left: 762px; top: 159px; }
  .copy-erp { left: 102px; top: 731px; }
  .copy-digital { left: 762px; top: 731px; }
  .indent-1 { padding-left: 46px; }
  .indent-2 { padding-left: 31px; }
  .indent-3 { padding-left: 8px; }

  .learn-more {
    position: absolute; width: 154px; height: 36px; border-radius: 18px; overflow: hidden;
    display: flex; text-decoration: none; color: #fff; font-size: 15px;
  }
  .learn-more .label { width: 119px; display: flex; align-items: center; justify-content: center; padding-top: 2px; }
  .learn-more .arrow { flex: 1; background: var(--btn-grey); position: relative; }
  .learn-more .arrow::after {
    content: ""; position: absolute; left: 12px; top: 12px;
    border-left: 9px solid #fff; border-top: 6px solid transparent; border-bottom: 6px solid transparent;
  }
  .btn-doc { left: 102px; top: 452px; background: var(--purple); }
  .btn-security { left: 869px; top: 452px; background: var(--green); }
  .btn-erp { left: 102px; top: 996px; background: var(--teal); }
  .btn-digital { left: 869px; top: 996px; background: var(--blue); }

  .line-icon { position: absolute; fill: none; stroke: var(--icon); stroke-width: 2.2; stroke-linecap: round; stroke-linejoin: round; }
</style>
</head>
<body>
<div class="canvas">
  <svg class="diagram" width="1134" height="1200" viewBox="0 0 1134 1200" aria-hidden="true">
    <defs>
      <clipPath id="clip-top-left"><path d="M70,124 A68,68 0 0 1 138,56 H446 A68,68 0 0 1 514,124 V541 H138 A68,68 0 0 1 70,473 Z"/></clipPath>
      <clipPath id="clip-top-right"><path d="M619,541 V124 A68,68 0 0 1 687,56 H995 A68,68 0 0 1 1063,124 V473 A68,68 0 0 1 995,541 Z"/></clipPath>
      <clipPath id="clip-bottom-left"><path d="M70,714 A68,68 0 0 1 138,646 H514 V1064 A68,68 0 0 1 446,1132 H138 A68,68 0 0 1 70,1064 Z"/></clipPath>
      <clipPath id="clip-bottom-right"><path d="M619,646 H995 A68,68 0 0 1 1063,714 V1064 A68,68 0 0 1 995,1132 H687 A68,68 0 0 1 619,1064 Z"/></clipPath>
    </defs>

    <g clip-path="url(#clip-top-left)">
      <rect x="60" y="50" width="460" height="500" fill="var(--card)"/>
      <rect x="60" y="50" width="460" height="78" fill="var(--purple)"/>
      <circle cx="567" cy="594" r="274" fill="var(--purple)"/>
    </g>
    <g clip-path="url(#clip-top-right)">
      <rect x="610" y="50" width="460" height="500" fill="var(--card)"/>
      <rect x="610" y="50" width="460" height="78" fill="var(--green)"/>
      <circle cx="567" cy="594" r="274" fill="var(--green)"/>
    </g>
    <g clip-path="url(#clip-bottom-left)">
      <rect x="60" y="640" width="460" height="500" fill="var(--card)"/>
      <rect x="60" y="1062" width="460" height="80" fill="var(--teal)"/>
      <circle cx="567" cy="594" r="274" fill="var(--teal)"/>
    </g>
    <g clip-path="url(#clip-bottom-right)">
      <rect x="610" y="640" width="460" height="500" fill="var(--card)"/>
      <rect x="610" y="1062" width="460" height="80" fill="var(--blue)"/>
      <circle cx="567" cy="594" r="274" fill="var(--blue)"/>
    </g>

    <circle cx="567" cy="594" r="213" fill="var(--ring)"/>
    <circle cx="567" cy="594" r="175" fill="var(--orange)"/>
  </svg>

  <!-- icons -->
  <svg class="line-icon" style="left:419px;top:161px" width="64" height="76" viewBox="0 0 64 76" aria-hidden="true">
    <rect x="20" y="3" width="40" height="58"/>
    <rect x="13" y="9" width="40" height="58" fill="var(--card)"/>
    <rect x="4" y="15" width="40" height="58" fill="var(--card)"/>
    <path d="M10,24 H38 M10,30 H38 M10,36 H38 M10,42 H38 M10,48 H38 M10,54 H38 M10,60 H38 M10,66 H38"/>
  </svg>
  <svg class="line-icon" style="left:656px;top:161px" width="74" height="76" viewBox="0 0 74 76" aria-hidden="true">
    <path d="M37,4 C27,11 17,13 8,12 V36 C8,52 20,62 37,70 C54,62 66,52 66,36 V12 C57,13 47,11 37,4 Z"/>
    <path d="M37,12 C29,17 22,19 15,19 V36 C15,48 24,56 37,62 C50,56 59,48 59,36 V19 C52,19 45,17 37,12 Z"/>
    <rect x="27" y="35" width="20" height="16" rx="2"/>
    <path d="M31,35 V29 A6,6 0 0 1 43,29 V35 M37,41 V46"/>
    <path d="M2,73 H72"/>
  </svg>
  <svg class="line-icon" style="left:407px;top:941px" width="76" height="74" viewBox="0 0 76 74" aria-hidden="true">
    <circle cx="52" cy="20" r="13" stroke-width="5" stroke-dasharray="4 4"/>
    <circle cx="52" cy="20" r="9"/>
    <circle cx="52" cy="20" r="4"/>
    <circle cx="24" cy="48" r="15" stroke-width="5" stroke-dasharray="4.5 4.5"/>
    <circle cx="24" cy="48" r="11"/>
    <circle cx="24" cy="48" r="5"/>
    <circle cx="26" cy="6" r="4"/>
    <circle cx="8" cy="22" r="3"/>
    <path d="M58,46 H68 M58,52 H68 M58,58 H68 M58,64 H68 M58,70 H68 M63,42 V72"/>
  </svg>
  <svg class="line-icon" style="left:655px;top:941px" width="76" height="74" viewBox="0 0 76 74" aria-hidden="true">
    <circle cx="38" cy="34" r="28" stroke-width="6" stroke-dasharray="6 6"/>
    <circle cx="38" cy="34" r="24"/>
    <circle cx="38" cy="34" r="16"/>
    <ellipse cx="38" cy="34" rx="7" ry="16"/>
    <path d="M22,34 H54 M25,26 H51 M25,42 H51 M38,18 V50"/>
    <path d="M6,72 H70"/>
  </svg>

  <h2 class="card-title top-left">Document Management</h2>
  <h2 class="card-title top-right">Security and Compliance</h2>
  <h2 class="card-title bottom-left">Enterprise Resource Planning</h2>
  <h2 class="card-title bottom-right">Digital Transformation</h2>

  <div class="core-title">SUPER<br>PRODUCT</div>

  <div class="card-copy copy-doc">
    <p>Streamline document organization,<br>access, and collaboration with<br>easier file storage and sharing,<br>leading to more efficient<br>workflows.</p>
    <ul>
      <li>Centralize Document Center</li>
      <li>Collaborative Workspace<br>Integration</li>
      <li>Automated Compliance<br>Tracking</li>
      <li>Check 4</li>
    </ul>
  </div>

  <div class="card-copy copy-security">
    <p>Benefit from tailored cloud<br>solutions, secure data storage,<br>and expert disaster recovery<br>planning for reliable and scalable<br>IT operations.</p>
    <ul>
      <li>Custom Cloud Solutions</li>
      <li>Secure Data Storage</li>
      <li>Expert Disaster Recovery</li>
      <li>Check 4</li>
    </ul>
  </div>

  <div class="card-copy copy-erp">
    <p>Simplify management<br>across finance, sales, and<br>operations, enabling better<br>decision-making and improved<br>productivity.</p>
    <ul>
      <li>Integrated Business Processes</li>
      <li>Enhanced Decision-Making</li>
      <li>Productivity Improvement</li>
      <li>Check 4</li>
    </ul>
  </div>

  <div class="card-copy copy-digital">
    <p class="indent-1">Turn scanned document</p>
    <p class="indent-2">into easily searchable digital</p>
    <p class="indent-3">archives, boosting efficiency and</p>
    <p>accessibility.</p>
    <ul>
      <li>Instant searchable Archives<br>with OCR</li>
      <li>Automated Document<br>Classification</li>
      <li>DocuHub and Cloud Blob<br>Ready</li>
      <li>Check 4</li>
    </ul>
  </div>

  <a class="learn-more btn-doc" href="#"><span class="label">Learn More</span><span class="arrow"></span></a>
  <a class="learn-more btn-security" href="#"><span class="label">Learn More</span><span class="arrow"></span></a>
  <a class="learn-more btn-erp" href="#"><span class="label">Learn More</span><span class="arrow"></span></a>
  <a class="learn-more btn-digital" href="#"><span class="label">Learn More</span><span class="arrow"></span></a>
</div>
</body>
</html>
```